Antibacterial Hand Wash Squeeze Tube Label

We're looking for a contemporary label design for a new Antibacterial Hand Wash for an 8oz squeeze tube. The new consumer brand will be sold to consumers in major US retail stores & online. The moisturizing hand wash contains Aloe Vera, vitamin E, and other natural ingredients so the design should include the color green. Real photos are very effective on packaging, so a picture of Aloe Vera or possibly two hands washing would help draw consumers' attention to the tube on the retail shelf. The front label may wrap around the sides. Rear must be left mostly blank
US Consumers - retail stores & online
Consumer

```html
<!DOCTYPE html>
<html lang="en">
<head>
<meta charset="utf-8">
<title>Verdane Hand Wash Tube Label</title>
<link rel="stylesheet" href="https://fonts.googleapis.com/css2?family=Quicksand:wght@600;700&family=Montserrat:wght@800&display=swap">
<style>
  :root {
    --backdrop: #f2f4f1;
    --leaf-deep: #0f5f2a;
    --leaf-mid: #2e9a46;
    --leaf-light: #74b843;
    --silver-light: #f1f3f2;
    --silver-dark: #8f9595;
    --badge-green: #1f6e35;
    --art-pale: #c9e8ad;
    --art-soft: #8ccb68;
    --ink-white: #ffffff;
  }
  html, body {
    margin: 0;
    width: 1200px;
    height: 1000px;
    overflow: hidden;
    background: var(--backdrop);
  }
  .canvas {
    position: relative;
    width: 1200px;
    height: 1000px;
  }
  .tube-label {
    position: absolute;
    left: 400px;
    top: 100px;
    width: 400px;
    height: 800px;
    display: block;
  }
  .brand-name {
    font-family: "Quicksand", sans-serif;
    font-weight: 700;
    font-size: 68px;
    fill: var(--ink-white);
  }
  .badge-text {
    font-family: "Montserrat", sans-serif;
    font-weight: 800;
    font-size: 13px;
    letter-spacing: 1px;
    fill: var(--badge-green);
  }
</style>
</head>
<body>
<main class="canvas">
  <svg class="tube-label" viewBox="0 0 400 800" xmlns="http://www.w3.org/2000/svg">
    <defs>
      <linearGradient id="header-shade" x1="0" y1="0" x2="1" y2="0">
        <stop offset="0" stop-color="var(--leaf-deep)"/>
        <stop offset="0.55" stop-color="var(--leaf-mid)"/>
        <stop offset="1" stop-color="var(--leaf-deep)"/>
      </linearGradient>
      <linearGradient id="silver-shade" x1="0" y1="0" x2="1" y2="0">
        <stop offset="0" stop-color="var(--silver-dark)"/>
        <stop offset="0.5" stop-color="var(--silver-light)"/>
        <stop offset="1" stop-color="var(--silver-dark)"/>
      </linearGradient>
      <linearGradient id="art-shade" x1="0" y1="0" x2="0" y2="1">
        <stop offset="0" stop-color="var(--art-pale)"/>
        <stop offset="1" stop-color="var(--art-soft)"/>
      </linearGradient>
      <path id="badge-arc-upper" d="M 136 671 A 64 64 0 0 1 264 671"/>
      <path id="badge-arc-lower" d="M 142 671 A 58 58 0 0 0 258 671"/>
    </defs>

    <rect class="label-base" x="0" y="0" width="400" height="800" fill="var(--leaf-light)"/>

    <path class="silver-band" d="M0 380 Q200 560 400 380 L400 396 Q200 578 0 396 Z" fill="url(#silver-shade)"/>

    <path class="header-panel" d="M0 0 H400 V380 Q200 560 0 380 Z" fill="url(#header-shade)"/>

    <rect class="ingredient-art" role="img"
          aria-label="Aloe vera and vitamin E ingredient artwork"
          x="95" y="55" width="210" height="395" rx="16"
          fill="url(#art-shade)" opacity="0.9"/>

    <text class="brand-name" x="200" y="562" text-anchor="middle">verdane</text>

    <g class="hand-wash-badge">
      <circle cx="200" cy="671" r="79" fill="url(#silver-shade)"/>
      <circle cx="200" cy="671" r="72" fill="#ffffff" opacity="0.85"/>
      <circle cx="200" cy="671" r="52" fill="var(--badge-green)"/>
      <circle class="badge-hands-art" role="img" aria-label="Two hands washing with soap lather"
              cx="200" cy="671" r="44" fill="#e9b894" opacity="0.85"/>
      <text class="badge-text"><textPath href="#badge-arc-upper" startOffset="50%" text-anchor="middle">HAND WASH</textPath></text>
      <text class="badge-text" dy="12"><textPath href="#badge-arc-lower" startOffset="50%" text-anchor="middle">100 ML</textPath></text>
    </g>
  </svg>
</main>
</body>
</html>
```